Global (re)insurance broker needs a business card design

We need a classic business card for our company that is headquartered in SG, with offices in Malaysia and Dubai. We specialise in insurance and reinsurance broking and consultancy for our global clients.

```html
<!DOCTYPE html>
<html lang="en">
<head>
<meta charset="UTF-8">
<title>Kestran Business Card</title>
<link href="https://fonts.googleapis.com/css2?family=Montserrat:wght@400;500;700&display=swap" rel="stylesheet">
<style>
  :root {
    --page-bg: #e9eaec;
    --card-white: #ffffff;
    --brand-blue: #264896;
    --brand-green: #c2dbb7;
    --ink: #1d1d1f;
    --ink-soft: #3a3a3c;
  }
  * { box-sizing: border-box; margin: 0; padding: 0; }
  html, body {
    width: 1200px; height: 1200px; overflow: hidden;
    background: var(--page-bg);
    font-family: "Montserrat", sans-serif;
  }
  .stage {
    position: relative; width: 1200px; height: 1200px;
  }
  .card {
    position: absolute; left: 250px;
    width: 700px; height: 400px;
    border-radius: 28px; overflow: hidden;
    box-shadow: 0 14px 34px rgba(0,0,0,0.18);
  }
  .card--front { top: 130px; background: var(--card-white); }
  .card--back  { top: 670px; background: var(--brand-blue); }

  .front-bands { position: absolute; inset: 0; width: 700px; height: 400px; }

  .front-wordmark {
    position: absolute; right: 70px; top: 118px;
    font-weight: 700; font-size: 62px; letter-spacing: 2px;
    color: var(--brand-blue);
  }

  .holder { position: absolute; left: 52px; top: 188px; }
  .holder__name {
    font-weight: 700; font-size: 30px; letter-spacing: -0.5px;
    color: var(--brand-blue); line-height: 1;
  }
  .holder__role {
    font-weight: 400; font-size: 19px; letter-spacing: 0.5px;
    color: var(--ink-soft); margin-top: 4px;
  }
  .contacts { list-style: none; margin-top: 12px; margin-left: 14px; }
  .contacts li {
    display: flex; align-items: flex-start; gap: 10px;
    font-size: 15px; font-weight: 500; color: var(--ink);
    line-height: 1.3; margin-bottom: 3px;
  }
  .contacts svg { width: 16px; height: 16px; flex: none; margin-top: 2px; fill: var(--brand-blue); }

  .back-wordmark {
    position: absolute; left: 0; right: 0; top: 50%;
    transform: translateY(-50%);
    text-align: center;
    font-weight: 700; font-size: 104px; letter-spacing: 4px;
    color: var(--card-white);
  }
</style>
</head>
<body>
<main class="stage">
  <section class="card card--front">
    <svg class="front-bands" viewBox="0 0 700 400" aria-hidden="true">
      <polygon points="0,388 452,352 452,400 0,400" fill="var(--brand-blue)"/>
      <polygon points="466,350 700,330 700,400 466,400" fill="var(--brand-green)"/>
    </svg>

    <div class="front-wordmark">KESTRAN</div>

    <div class="holder">
      <h1 class="holder__name">FULL NAME</h1>
      <p class="holder__role">POSITION</p>
      <ul class="contacts">
        <li>
          <svg viewBox="0 0 24 24"><path d="M6.6 10.8a15.1 15.1 0 0 0 6.6 6.6l2.2-2.2a1 1 0 0 1 1-.25 11.4 11.4 0 0 0 3.6.57 1 1 0 0 1 1 1V20a1 1 0 0 1-1 1A17 17 0 0 1 3 4a1 1 0 0 1 1-1h3.5a1 1 0 0 1 1 1c0 1.25.2 2.45.57 3.6a1 1 0 0 1-.25 1z"/></svg>
          <span>(000) 000 0000</span>
        </li>
        <li>
          <svg viewBox="0 0 24 24"><path d="M2 5h20v14H2z M3 6l9 7 9-7" fill="none" stroke="var(--brand-blue)" stroke-width="2.4"/></svg>
          <span>email@company.com</span>
        </li>
        <li>
          <svg viewBox="0 0 24 24"><g fill="none" stroke="var(--brand-blue)" stroke-width="2"><circle cx="12" cy="12" r="9.5"/><ellipse cx="12" cy="12" rx="4" ry="9.5"/><path d="M2.5 12h19M4 7h16M4 17h16"/></g></svg>
          <span>www.company.com</span>
        </li>
        <li>
          <svg viewBox="0 0 24 24"><path d="M12 2a7 7 0 0 0-7 7c0 5.2 7 13 7 13s7-7.8 7-13a7 7 0 0 0-7-7zm0 9.5A2.5 2.5 0 1 1 12 6.5a2.5 2.5 0 0 1 0 5z"/></svg>
          <span>123 Name Street, 000<br>Your City, 00000-000</span>
        </li>
      </ul>
    </div>
  </section>

  <section class="card card--back">
    <div class="back-wordmark">KESTRAN</div>
  </section>
</main>
</body>
</html>
```